Oil & Gas Energy Consultancy Service

I am an experienced Upper Management former employed by a Global Service Company to the Oil & Gas Industry.
After 22 years I have decided to go as a Consultant working mainly in the same,(upper management) areas of work.
This is a, "One Man" operation.
Updates

Thank you all for your interest and professionalism in this little project.

It was hard to decide on a final contestant but it had to come down to one selection.
Best of luck with your other work & projects!
Tavo Renzi-Marlowe

Industry/Entity Type

Industry

Contact Information for Business Card

Quelbran Energy Services, Inc
Tavo Renzi-Marlowe - Managing Director
O&G Consultants
Suite 1470, Tower 3, Morrow Ave, Edmonton, AB, T5K 9W4 Canada
250 555 0193 tavo.marlowe@quelbran.net

Logo Text

Quelbran Energy Services

Logo styles of interest
Abstract Logo

```html
<!DOCTYPE html>
<html lang="en">
<head>
<meta charset="utf-8">
<title>Quelbran Energy Services – Business Card</title>
<link rel="stylesheet" href="https://fonts.googleapis.com/css2?family=Exo+2:wght@600&family=PT+Sans+Narrow&display=swap">
<style>
  :root {
    --ink: #3a312b;
    --orange: #e07426;
    --paper-light: #ffffff;
    --paper-edge: #e6e7e8;
  }
  html, body {
    margin: 0;
    padding: 0;
    overflow: hidden;
    background: var(--paper-edge);
  }
  .card {
    position: relative;
    width: 1200px;
    height: 652px;
    overflow: hidden;
    background: radial-gradient(ellipse 70% 80% at 40% 35%, var(--paper-light) 0%, #f6f6f7 50%, var(--paper-edge) 100%);
    color: var(--ink);
  }
  .brand {
    position: absolute;
    left: 236px;
    top: 100px;
    display: flex;
    align-items: center;
    gap: 18px;
  }
  .brand-square {
    width: 34px;
    height: 34px;
    background: var(--orange);
  }
  .brand-name {
    font-family: "Exo 2", sans-serif;
    font-weight: 600;
    font-size: 54px;
    line-height: 1;
    color: var(--ink);
    letter-spacing: 0.5px;
  }
  .holder {
    position: absolute;
    left: 168px;
    top: 330px;
    width: 372px;
    text-align: center;
  }
  .holder-name {
    font-family: "Exo 2", sans-serif;
    font-weight: 600;
    font-size: 44px;
    line-height: 1;
    margin: 0;
    padding-bottom: 8px;
    border-bottom: 2px solid var(--orange);
    white-space: nowrap;
  }
  .holder-role {
    font-family: "PT Sans Narrow", sans-serif;
    font-size: 31px;
    margin: 6px 0 0;
    line-height: 1.1;
  }
  .contact {
    position: absolute;
    left: 700px;
    top: 332px;
    margin: 0;
    padding: 0;
    list-style: none;
    font-family: "PT Sans Narrow", sans-serif;
    font-size: 33px;
    line-height: 42.5px;
    color: var(--ink);
  }
  .contact li {
    display: flex;
    align-items: flex-start;
  }
  .contact .icon {
    width: 30px;
    height: 30px;
    margin: 6px 26px 0 0;
    flex: none;
    fill: var(--ink);
  }
  .contact address {
    font-style: normal;
  }
  .bands {
    position: absolute;
    left: 0;
    bottom: 0;
    width: 1200px;
    height: 56px;
  }
  .band-dark { fill: var(--ink); }
  .band-orange { fill: var(--orange); }
</style>
</head>
<body>
<main class="card">
  <div class="brand">
    <span class="brand-square" aria-hidden="true"></span>
    <span class="brand-name">Quelbran Energy Services, Inc</span>
  </div>

  <div class="holder">
    <h1 class="holder-name">Tavo Renzi-Marlowe</h1>
    <p class="holder-role">O&amp;G Consultants</p>
  </div>

  <ul class="contact">
    <li>
      <svg class="icon" viewBox="0 0 30 30" aria-hidden="true">
        <rect x="9" y="4" width="12" height="22" rx="2"/>
        <rect x="11.5" y="7" width="7" height="7" fill="#fff"/>
        <rect x="13" y="1" width="2" height="4"/>
      </svg>
      <span>250 555 0193</span>
    </li>
    <li>
      <svg class="icon" viewBox="0 0 30 30" aria-hidden="true">
        <path d="M15 3 L2 15 L5 15 L5 27 L12 27 L12 19 L18 19 L18 27 L25 27 L25 15 L28 15 L23 10.4 L23 4 L20 4 L20 7.6 Z"/>
        <path d="M15 7 L8 13.5 L8 24 L10 24 L10 17 L20 17 L20 24 L22 24 L22 13.5 Z" fill="#fff"/>
      </svg>
      <address>Suite 1470, Tower 3<br>Morrow Ave, Edmonton<br>AB, T5K 9W4 Canada</address>
    </li>
    <li>
      <svg class="icon" viewBox="0 0 30 30" aria-hidden="true">
        <path d="M3 7 H27 V24 H3 Z M5.5 9 L15 16.5 L24.5 9 Z M5 10.5 V22 H25 V10.5 L15 18.5 Z" fill-rule="evenodd"/>
      </svg>
      <span>tavo.marlowe@quelbran.net</span>
    </li>
  </ul>

  <svg class="bands" viewBox="0 0 1200 56" aria-hidden="true">
    <polygon class="band-dark" points="361,0 504,0 486,56 341,56"/>
    <polygon class="band-orange" points="523,0 1200,0 1200,56 503,56"/>
  </svg>
</main>
</body>
</html>
```